Modern Minimalistic Supplement Label

Opportunity for recurring projects with a growing company. We have provided a detailed creative brief and all necessary files and guidelines. If you have any questions we will be closely monitoring the discussion board and email provided.

THE NAMES LISTED IN THE BRIEF ARE DIFFERENT FROM THE LABEL TEMPLATES. This is a private label brand. The label templates given are generic so please examine the entire brief before starting.

Use the PSD mockups attached and pair the labels with the correct bottles.

Do not use an entirely white background.

This could be excellent portfolio material.

Start by looking at the "CREATIVE_BRIEF" file. Logo files are contained in the "67046451" zip file.

UPDATE* Use the following business address for the "manufactured for" box on the labels.

Bramwell
4817 Pelton Ave. #2096
Ann Arbor MI 48276

Target Market(s)

All information provided in "CREATIVE_BRIEF" file.

Industry/Entity Type

Supplement

Requirements
Must have
• All information provided in "CREATIVE_BRIEF" file.
Nice to have
Should not have

```html
<!DOCTYPE html>
<html lang="en">
<head>
<meta charset="utf-8">
<title>Bramwell Steadfast Stride – Amino Blend Label</title>
<link rel="stylesheet" href="https://fonts.googleapis.com/css2?family=Josefin+Sans:wght@400;700&family=Roboto+Condensed:wght@300;400&display=swap">
<style>
  :root {
    --ink: #0d0d0e;
    --ink-soft: #1c1c1e;
    --rock: #3a3b3f;
    --rock-dark: #242528;
    --white: #ffffff;
    --grey-text: #d9d9d9;
    --pink: #e0236a;
    --pink-deep: #b81e55;
    --pink-mid: #d12864;
    --pink-light: #e84a82;
  }
  * { margin: 0; padding: 0; box-sizing: border-box; }
  html, body {
    width: 1200px;
    height: 1200px;
    overflow: hidden;
    background: var(--ink);
  }
  .label {
    position: relative;
    width: 1200px;
    height: 1200px;
    background: linear-gradient(180deg, var(--ink-soft) 0%, var(--ink) 55%);
    overflow: hidden;
    font-family: "Josefin Sans", sans-serif;
    color: var(--white);
  }
  .mountain-art {
    position: absolute;
    left: 0;
    top: 380px;
    width: 1200px;
    height: 460px;
    background:
      radial-gradient(ellipse 260px 380px at 170px 420px, var(--rock) 0%, var(--rock-dark) 60%, transparent 100%),
      radial-gradient(ellipse 220px 300px at 1060px 440px, var(--rock) 0%, var(--rock-dark) 60%, transparent 100%),
      radial-gradient(ellipse 300px 200px at 700px 460px, var(--rock-dark) 0%, transparent 100%);
    opacity: 0.9;
  }
  .brand {
    position: absolute;
    top: 260px;
    left: 0;
    width: 100%;
    display: flex;
    justify-content: center;
    align-items: center;
    gap: 16px;
  }
  .brand-mark {
    width: 18px;
    height: 18px;
    background: var(--white);
  }
  .brand-name {
    font-weight: 700;
    font-size: 44px;
    letter-spacing: 6px;
    line-height: 1;
  }
  .product-title {
    position: absolute;
    top: 410px;
    left: 0;
    width: 100%;
    text-align: center;
    font-weight: 700;
    line-height: 1;
  }
  .product-title .line-one {
    display: block;
    font-size: 122px;
    letter-spacing: 4px;
  }
  .product-title .line-two {
    display: block;
    font-size: 122px;
    letter-spacing: 10px;
    margin-top: 14px;
  }
  .product-variant {
    position: absolute;
    top: 725px;
    left: 0;
    width: 100%;
    text-align: center;
    font-family: "Roboto Condensed", sans-serif;
    font-weight: 300;
    font-size: 26px;
    letter-spacing: 9px;
    color: var(--grey-text);
  }
  .wave-band {
    position: absolute;
    left: 0;
    top: 790px;
    width: 1200px;
    height: 410px;
  }
  .claim {
    position: absolute;
    top: 955px;
    left: 0;
    width: 100%;
    text-align: center;
    font-family: "Roboto Condensed", sans-serif;
    font-weight: 300;
    font-size: 36px;
    letter-spacing: 3px;
  }
  .net-weight {
    position: absolute;
    top: 1025px;
    left: 0;
    width: 100%;
    text-align: center;
    font-family: "Roboto Condensed", sans-serif;
    font-weight: 300;
    font-size: 33px;
    letter-spacing: 0.5px;
  }
</style>
</head>
<body>
  <main class="label">
    <div class="mountain-art" role="img" aria-label="Sketched grey mountain range behind the product name"></div>

    <div class="brand">
      <span class="brand-mark"></span>
      <span class="brand-name">BRAMWELL</span>
    </div>

    <h1 class="product-title">
      <span class="line-one">STEADFAST</span>
      <span class="line-two">STRIDE</span>
    </h1>

    <p class="product-variant">AMINO BLEND | RASPBERRY</p>

    <svg class="wave-band" viewBox="0 0 1200 410" preserveAspectRatio="none" aria-hidden="true">
      <path d="M0 20 C 200 10, 380 80, 560 90 C 760 100, 900 40, 1200 60 L1200 410 L0 410 Z" fill="var(--pink-deep)"/>
      <path d="M0 50 C 220 40, 400 110, 600 110 C 800 110, 960 70, 1200 90 L1200 410 L0 410 Z" fill="var(--pink-mid)"/>
      <path d="M0 90 C 240 80, 420 150, 620 145 C 820 140, 980 110, 1200 130 L1200 410 L0 410 Z" fill="var(--pink)"/>
      <path d="M0 150 C 260 140, 460 190, 660 185 C 860 180, 1000 160, 1200 175 L1200 410 L0 410 Z" fill="var(--pink-light)" opacity="0.35"/>
    </svg>

    <p class="claim">FOR IMPROVED ENDURANCE</p>
    <p class="net-weight">NET WT. 360 G ( 12.7 OZ ) | DIETARY SUPPLEMENT</p>
  </main>
</body>
</html>
```